Modern home page design for a motel accommodation business

-The design must be based around the attached HPID (home page information design) called Velkirn HPID. I've attached Word and PDF versions - these are the same. The table boxes are just for approximate placement of information – you DON'T have to box everything in. All fonts used in the HPID are only examples - you can use any Google font you wish.

- Information only is in orange text. Copy to go on the design in black text. Some instructions are in the HPID. Please be creative!

-The design needs to be modern. Colours are to be black and white with burgundy and gray ...like the logo colours.

- I've provided the images for the galleries - they are labelled and will match the name in the HPID. Please use the supplied images!

- Examples of some websites that have great design... don't copy them please but they are similar in look to what we are after....
http://www.quillmerebnb.co.nz/
http://www.varlo.co.nz/
http://www.galventrishotel.co.nz/

Width of content will be 1100 pixels when implemented as a web page. Header height (without nav bar) 150-160 pixels.

I've allowed extra time for this design as it's a holiday time for many countries around the world.

If your design is chosen the winning PSD file will have to be provided as follows…
1. Canvas size of 2000px x 2000px - 72ppi in Adobe Photoshop (CS5 compatible)
2. Width of content section is 1100px wide - centered in the canvas
3. Any button rollovers/hovers in the PSD as hidden layers.
4. All fonts used must be Google fonts (except for the fonts in the header at the top of the page).
5. You will need to supply the chosen home page plus one example page (example page as a style guide for how all other pages will look). Example page is only the header and navigational bar at the top, an empty sector in the middle with a column (180 px wide) which can be left or right aligned which means the main sector is 920 pixels wide, and then the footer at the bottom of the page

```html
<!DOCTYPE html>
<html lang="en">
<head>
<meta charset="utf-8">
<title>Velkirn Court Motor Lodge</title>
<link href="https://fonts.googleapis.com/css2?family=Open+Sans:ital,wght@0,400;0,600;0,700;1,400&family=Playfair+Display:wght@400;700&display=swap" rel="stylesheet">
<style>
:root{
  --burgundy:#5e0a1f;
  --burgundy-deep:#4f0818;
  --accent:#b3123a;
  --ink:#222;
  --grey:#888;
  --grey-light:#f1f1f1;
  --line:#dcdcdc;
  --white:#fff;
}
*{box-sizing:border-box;margin:0;padding:0}
html,body{width:913px;height:1200px;overflow:hidden;background:var(--white)}
body{font-family:"Open Sans",Arial,sans-serif;color:var(--ink)}
.page{position:relative;width:913px;height:1200px;overflow:hidden}
.abs{position:absolute}

/* header */
.brand{left:206px;top:14px;display:flex;align-items:center;gap:7px}
.brand-mark{width:14px;height:14px;background:var(--burgundy)}
.brand-name{font-family:"Playfair Display",serif;font-weight:700;font-size:14px;line-height:1.15;color:var(--burgundy);text-transform:uppercase;letter-spacing:.5px}
.recommend{left:396px;top:36px;font-size:4.5px;color:#444;letter-spacing:.2px}
.recommend strong{display:block;font-family:"Open Sans",sans-serif;font-weight:600;font-size:13px;color:#333;letter-spacing:0;margin-top:1px}
.header-info{right:205px;top:20px;text-align:right}
.header-info h2{font-family:"Playfair Display",serif;font-size:6.5px;font-weight:700;line-height:1.25;text-transform:uppercase;color:var(--ink)}
.phone-line{display:flex;justify-content:flex-end;align-items:center;gap:5px;margin-top:4px;font-size:5.5px;line-height:1.25}
.book-link{display:block;margin-top:11px;font-family:"Playfair Display",serif;font-weight:700;font-size:7px;color:var(--burgundy);text-transform:uppercase}

/* nav */
.nav{left:0;top:91px;width:913px;height:30px;background:var(--burgundy)}
.nav ul{list-style:none;position:absolute;left:206px;width:502px;top:0;height:30px;display:flex;justify-content:space-between;align-items:center}
.nav li{font-size:6.8px;color:var(--white);text-transform:uppercase}

/* hero */
.hero{left:0;top:121px;width:913px;height:251px;background:linear-gradient(90deg,#6f6a62 0%,#4a5a52 25%,#6c7d8e 50%,#55606b 75%,#5f6b5e 100%)}
.hero-title{left:0;top:207px;width:913px;text-align:center;font-family:"Playfair Display",serif;font-weight:700;font-size:27px;line-height:31px;color:var(--white)}
.hero-btn{left:402px;top:286px;width:107px;height:24px;border:1px solid var(--white);outline:1px solid rgba(255,255,255,.7);outline-offset:2px;color:var(--white);font-size:6.8px;text-transform:uppercase;display:flex;align-items:center;justify-content:center}

/* booking */
.booking{left:551px;top:361px;width:157px;height:188px;background:var(--burgundy)}
.booking label{position:absolute;left:23px;font-size:6px;color:var(--white)}
.field{position:absolute;left:23px;width:110px;height:19px;background:var(--white);display:flex;align-items:center;gap:5px;padding:0 6px;font-size:6.5px;color:#333}
.field.select{justify-content:space-between}
.reserve-btn{position:absolute;left:24px;top:150px;width:109px;height:23px;border:1px solid var(--white);outline:1px solid rgba(255,255,255,.6);outline-offset:-3px;color:var(--white);font-size:6.5px;text-transform:uppercase;display:flex;align-items:center;justify-content:center}

/* accommodation */
.accom-title{left:206px;top:404px;font-family:"Playfair Display",serif;font-weight:700;font-size:12px;line-height:13.5px}
.accom-list{left:206px;top:442px;width:107px;list-style:none}
.accom-list li{font-size:6.3px;color:var(--grey);height:16.5px;line-height:16.5px;position:relative}
.accom-list li.active{color:var(--accent);border-top:1px solid var(--line);border-bottom:1px solid var(--line)}
.accom-list li.active::after{content:"";position:absolute;right:2px;top:5px;width:4px;height:4px;border-right:1px solid #aaa;border-top:1px solid #aaa;transform:rotate(45deg)}
.accom-photo{left:315px;top:405px;width:206px;height:132px;background:linear-gradient(100deg,#c47a2a 0%,#c9a66f 20%,#d9cbb0 50%,#8e7d6a 80%,#5a4a3a 100%)}
.accom-caption{left:315px;top:542px;width:206px;text-align:right;font-size:6.3px;color:#555}

/* why stay */
.why{left:0;top:589px;width:913px;height:235px;background:var(--grey-light)}
.why-title{left:206px;top:617px;font-family:"Playfair Display",serif;font-weight:700;font-size:11.5px}
.ticks{left:206px;top:648px;list-style:none}
.ticks li{font-size:6.3px;color:var(--grey);height:11px;display:flex;align-items:center;gap:5px}
.why-text{left:206px;top:713px;width:240px;font-size:6.3px;line-height:11px;color:var(--grey)}
.video{left:467px;top:649px;width:241px;height:134px;background:linear-gradient(180deg,#d8c9a8 0%,#9c8060 45%,#7a6a55 100%)}
.video-bar{position:absolute;left:0;top:0;width:100%;height:10px;background:rgba(20,20,20,.85);color:var(--white);font-size:4.8px;line-height:10px;padding-left:4px}
.video-play{position:absolute;left:105px;top:58px}

/* testimonial */
.short-quote{left:206px;top:864px;font-size:6.3px;font-style:italic;color:#555}
.quote-source{left:224px;top:877px;font-size:11px;font-weight:600;color:#333}
.quote{left:389px;top:866px;width:319px;font-size:6.3px;line-height:11px;font-style:italic;color:var(--grey)}
.quote-author{left:389px;top:904px;width:319px;text-align:right;font-size:6.3px;color:#555}

/* footer */
.footer{left:0;top:948px;width:913px;height:252px;background:var(--burgundy-deep)}
.foot-links{left:206px;list-style:none}
.foot-links li{font-size:6.3px;color:var(--white);line-height:11px}
.foot-links li.head{font-weight:700}
.badge{background:var(--white);border-radius:2px}
.badge-inner{position:absolute;left:4px;top:4px;right:4px;bottom:4px;background:#5a9e3a}
.badge-grey{background:linear-gradient(180deg,#d6d6d6,#8d8d8d);border-radius:3px}
.badge-blue{background:#1e3f8f}
.badge-white{background:var(--white)}
.badge-caption{left:407px;top:1022px;font-size:6.3px;color:var(--white)}
.awards-text{left:407px;top:1095px;width:118px;font-size:6.3px;line-height:11px;color:var(--white);text-align:justify}
.map{left:561px;top:959px;width:147px;height:123px;background:linear-gradient(135deg,#e8e4d8 0%,#d9e3c8 45%,#e6e1d3 100%)}
.contact{left:561px;top:1095px;font-size:6.3px;line-height:11px;color:var(--white)}
.contact strong{font-weight:700}
.contact .hl{color:var(--accent)}
.social{left:561px;top:1155px;width:71px;height:20px;background:var(--white);display:flex;align-items:center;gap:4px;padding-left:3px}
.social-mark{width:13px;height:13px;background:#3b5998}
.social-name{font-size:6.5px;font-weight:600;color:#3b5998;line-height:1.1}
</style>
</head>
<body>
<div class="page">

  <header>
    <div class="abs brand">
      <span class="brand-mark"></span>
      <span class="brand-name">Velkirn Court<br>Motor Lodge</span>
    </div>
    <div class="abs recommend">RECOMMENDED ON:<strong>TripVista</strong></div>
    <div class="abs header-info">
      <h2>Motel accommodation<br>in central Christchurch</h2>
      <div class="phone-line">
        <svg width="9" height="9" viewBox="0 0 10 10"><circle cx="5" cy="5" r="5" fill="#222"/><path d="M3.2 2.6l1 1-.5.7c.4.8 1 1.4 1.8 1.8l.7-.5 1 1-.7.8C4.6 7.2 2.8 5.4 2.4 3.3z" fill="#fff"/></svg>
        <span>0800 4 VELKIRN | 0800 555 0142<br>+64 3 555 0198</span>
      </div>
      <span class="book-link">Book online!</span>
    </div>
  </header>

  <nav class="abs nav">
    <ul>
      <li>Home</li><li>About us</li><li>Accommodation</li><li>Policies &amp; Facilities</li><li>Book online</li><li>Local Christchurch info</li><li>Contact/map</li>
    </ul>
  </nav>

  <section>
    <div class="abs hero" role="img" aria-label="Motel exterior with sign, gabled turret roofs and garden courtyard"></div>
    <h1 class="abs hero-title">Top Motel Accommodation<br>in Central Christchurch</h1>
    <div class="abs hero-btn">Book online</div>
  </section>

  <form class="abs booking">
    <label style="top:24px">Check-in date:</label>
    <div class="field" style="top:34px">
      <svg width="9" height="8" viewBox="0 0 9 8"><rect x=".5" y="1" width="8" height="6.5" fill="none" stroke="#333" stroke-width=".8"/><path d="M2 3h1M4 3h1M6 3h1M2 5h1M4 5h1M6 5h1" stroke="#333" stroke-width=".8"/></svg>21/01/2015
    </div>
    <label style="top:63px">Check-out date:</label>
    <div class="field" style="top:74px">
      <svg width="9" height="8" viewBox="0 0 9 8"><rect x=".5" y="1" width="8" height="6.5" fill="none" stroke="#333" stroke-width=".8"/><path d="M2 3h1M4 3h1M6 3h1M2 5h1M4 5h1M6 5h1" stroke="#333" stroke-width=".8"/></svg>22/01/2015
    </div>
    <label style="top:103px">Room type:</label>
    <div class="field select" style="top:115px">Studio
      <svg width="10" height="6" viewBox="0 0 10 6"><path d="M1 1l4 4 4-4" fill="none" stroke="#333" stroke-width="1"/></svg>
    </div>
    <div class="reserve-btn">Online reservation</div>
  </form>

  <section>
    <h2 class="abs accom-title">Accommodation<br>options:</h2>
    <ul class="abs accom-list">
      <li>Studio</li><li>Studio Spa Unit</li><li>1 bedroom unit</li><li class="active">2 bedroom unit</li><li>Access unit</li>
    </ul>
    <div class="abs accom-photo" role="img" aria-label="Two bedroom unit interior with bed, armchair and windows"></div>
    <p class="abs accom-caption">2 Bedroom unit</p>
  </section>

  <section>
    <div class="abs why"></div>
    <h2 class="abs why-title">Why stay with Velkirn Court Motor Lodge?</h2>
    <ul class="abs ticks">
      <li><svg width="5" height="4" viewBox="0 0 5 4"><path d="M.5 2l1.3 1.3L4.5.5" fill="none" stroke="#888" stroke-width=".8"/></svg>Superb friendly service</li>
      <li><svg width="5" height="4" viewBox="0 0 5 4"><path d="M.5 2l1.3 1.3L4.5.5" fill="none" stroke="#888" stroke-width=".8"/></svg>Central city location on Harrow Ave (near Linden St &amp; CBD)</li>
      <li><svg width="5" height="4" viewBox="0 0 5 4"><path d="M.5 2l1.3 1.3L4.5.5" fill="none" stroke="#888" stroke-width=".8"/></svg>Free Wifi available in every room</li>
      <li><svg width="5" height="4" viewBox="0 0 5 4"><path d="M.5 2l1.3 1.3L4.5.5" fill="none" stroke="#888" stroke-width=".8"/></svg>42" plasma TVs with 50+ StreamBox channels</li>
      <li><svg width="5" height="4" viewBox="0 0 5 4"><path d="M.5 2l1.3 1.3L4.5.5" fill="none" stroke="#888" stroke-width=".8"/></svg>Self-contained, recently redecorated, large spacious rooms</li>
    </ul>
    <p class="abs why-text">Velkirn Court Motor Lodge offers affordable, comfortable, family friendly, central city motel accommodation in Christchurch, New Zealand.<br>Your hosts Maren and Tobias have recently refurbished the motel's 14 units, which have brand new luxurious beds, bedding, and new carpeting. We look forward to seeing you soon.</p>
    <div class="abs video" role="img" aria-label="Video still of the motel frontage with turret roof">
      <div class="video-bar">Velkirn Court Motor Lodge Christchurch</div>
      <svg class="video-play" width="30" height="20" viewBox="0 0 30 20"><circle cx="15" cy="10" r="10" fill="rgba(20,20,20,.8)"/><path d="M12 6l7 4-7 4z" fill="#fff"/></svg>
    </div>
  </section>

  <section>
    <p class="abs short-quote">"Excellent customer service as always"</p>
    <p class="abs quote-source">TripVista</p>
    <blockquote class="abs quote">" We always enjoy our stay there as Maren and Tobias have excellent customer service. We have stayed quite a few times and the customer service and the tidiness, and quiet of the rooms is always worth looking forward to. The CBD is close by with the Bean House and the Riverside Casino about 10 minutes walk. "</blockquote>
    <p class="abs quote-author">- Lena Hart</p>
  </section>

  <footer>
    <div class="abs footer"></div>
    <ul class="abs foot-links" style="top:956px">
      <li class="head">Home</li><li>About Us</li><li>Policies &amp; Facilities</li><li>Local Christchurch Info</li>
    </ul>
    <ul class="abs foot-links" style="top:1010px">
      <li class="head">Accommodation</li><li>Studio</li><li>Studio Spa Unit</li><li>1 bedroom unit</li><li>2 bedroom unit</li><li>Access unit</li>
    </ul>
    <div class="abs badge" style="left:307px;top:959px;width:71px;height:65px"><div class="badge-inner"></div></div>
    <div class="abs badge" style="left:307px;top:1034px;width:71px;height:66px"><div class="badge-inner"></div></div>
    <div class="abs badge-grey" style="left:307px;top:1112px;width:55px;height:62px"></div>
    <div class="abs badge-blue" style="left:407px;top:959px;width:80px;height:57px"></div>
    <p class="abs badge-caption">StreamBox Decoder</p>
    <div class="abs badge-white" style="left:407px;top:1043px;width:75px;height:39px"></div>
    <p class="abs awards-text">Winners of one of these exclusive awards consistently deliver superb service, an exceptional guest experience and notable value.</p>
    <div class="abs map" role="img" aria-label="Street map of central Christchurch showing the motel location"></div>
    <div class="abs contact">
      <strong>Contact Details:</strong><br>
      Your hosts: Maren and Tobias<br>
      0800 4 VELKIRN | 0800 555 0142<br>
      +64 3 555 0198 | <span class="hl">BOOK ONLINE</span><br>
      Email: velkirn.court@harbourmail.co.nz
    </div>
    <div class="abs social"><span class="social-mark"></span><span class="social-name">Find us on<br>Socialnet</span></div>
  </footer>

</div>
</body>
</html>
```